POP ART / Benny Lustrik type advertisment for medical practice

Our medical practice would like an ad resembling "Pop Art" / Benny Lustrik artwork.
We like outside-the-box advertisements and DO NOT want to look like a doctor's office / hospital / healthcare facility ad. It would be good to have an ad that can be used for full page and a modified one that could be used for quarter page ads that doesn't sacrifice the artistic vision you have created!
Reason: Would like more designs! Thanks!
Target Market(s)
adults 18-100+
Industry/Entity Type
Healthcare
Colors
Designer to choose colors to be used in the design.
Requirements
Must have
- must have photo of Dr. Tolliver
- his name Hugo Tolliver, MD
- the practice logo
- the address: 41587 Calder Ridge Road, Suite 215, Mission Viejo, CA 92691
- phone: 949-555-0178
- website: www.quillmarshvale.net
- tag line: Modern Medicine, Traditional Care
Nice to have
- family practice
- open daily
- book online
Should not have
- look like a doctor office or healthcare facility ad

```html
<!DOCTYPE html>
<html lang="en">
<head>
<meta charset="utf-8">
<title>Hugo Tolliver, MD – Family Practice</title>
<link rel="stylesheet" href="https://fonts.googleapis.com/css2?family=Montserrat:wght@500;700;800&family=Pacifico&display=swap">
<style>
  :root {
    --pop-pink: #e4007f;
    --pop-yellow: #ffe800;
    --pop-blue: #0a9ee0;
    --pale-yellow: #fff27a;
    --shadow-red: #e5142b;
    --ink: #141210;
    --paper: #ffffff;
    --skin: #f4b98c;
    --hair: #e8b81a;
    --brand-green: #1e6b2f;
  }
  * { margin: 0; padding: 0; box-sizing: border-box; }
  html, body {
    width: 1200px; height: 1200px;
    overflow: hidden;
    background: var(--paper);
  }
  .ad {
    position: absolute;
    left: 136px; top: 0;
    width: 928px; height: 1200px;
    background: var(--pop-pink);
    overflow: hidden;
  }
  .ad-art { position: absolute; inset: 0; width: 928px; height: 1200px; }
  .side-label {
    font-family: "Montserrat", sans-serif;
    font-weight: 500;
    font-size: 104px;
  }
  .side-label--family { fill: var(--pop-yellow); }
  .side-label--open { fill: var(--pop-blue); }
  .doctor-name {
    font-family: "Pacifico", cursive;
    font-size: 100px;
    fill: var(--paper);
    stroke: var(--ink);
    stroke-width: 12px;
    stroke-linejoin: round;
    paint-order: stroke fill;
  }
  .tagline {
    font-family: "Montserrat", sans-serif;
    font-weight: 800;
    font-size: 37px;
    stroke: var(--ink);
    stroke-width: 7px;
    stroke-linejoin: round;
    paint-order: stroke fill;
  }
  .tagline .t-blue { fill: var(--pop-blue); }
  .tagline .t-pink { fill: var(--pop-pink); }
  .tagline .t-yellow { fill: var(--pop-yellow); }

  .contact-panel {
    position: absolute;
    left: 0; top: 1036px;
    width: 464px; height: 128px;
    background: var(--pale-yellow);
    padding: 14px 0 0 54px;
    font-family: "Montserrat", sans-serif;
    font-weight: 700;
    font-size: 18.5px;
    line-height: 27px;
    color: var(--pop-pink);
    text-transform: uppercase;
    white-space: nowrap;
  }
  .brand-panel {
    position: absolute;
    left: 464px; top: 1036px;
    width: 464px; height: 132px;
    background: var(--paper);
    display: flex;
    align-items: center;
    padding-left: 40px;
    gap: 14px;
  }
  .brand-mark {
    width: 66px; height: 66px;
    background: var(--brand-green);
    flex: none;
  }
  .brand-name {
    font-family: "Montserrat", sans-serif;
    font-weight: 700;
    color: var(--brand-green);
    line-height: 1;
  }
  .brand-name .brand-main { display: block; font-size: 38px; letter-spacing: -0.5px; }
  .brand-name .brand-sub { display: block; font-size: 15px; letter-spacing: 9px; margin-top: 8px; }
</style>
</head>
<body>
  <main class="ad">
    <svg class="ad-art" viewBox="0 0 928 1200" xmlns="http://www.w3.org/2000/svg">
      <defs>
        <linearGradient id="portraitTones" x1="0" y1="0" x2="0" y2="1">
          <stop offset="0" stop-color="var(--hair)"/>
          <stop offset="0.3" stop-color="var(--hair)"/>
          <stop offset="0.42" stop-color="var(--skin)"/>
          <stop offset="0.62" stop-color="var(--skin)"/>
          <stop offset="0.7" stop-color="var(--ink)"/>
          <stop offset="1" stop-color="var(--ink)"/>
        </linearGradient>
      </defs>

      <path class="portrait-offset" fill="var(--shadow-red)"
        d="M412 10 C300 20 200 110 172 240 L210 560 L300 744 L52 864 L-8 1200 L40 1200 L40 900 Z"/>
      <path class="portrait" role="img" aria-label="Pop art portrait of Dr. Hugo Tolliver in a dark suit and tie"
        fill="url(#portraitTones)"
        d="M424 16 C560 10 680 50 704 120 C730 200 740 300 736 400 L712 640 L928 744 L928 1200 L0 1200 L0 1040 L64 864 L312 744 L224 560 L184 240 C210 110 300 22 424 16 Z"/>

      <text class="side-label side-label--family" transform="translate(842 16) rotate(90)"
        textLength="912" lengthAdjust="spacingAndGlyphs">FAMILY PRACTICE</text>
      <text class="side-label side-label--open" transform="translate(88 1028) rotate(-90)"
        textLength="652" lengthAdjust="spacingAndGlyphs">OPEN DAILY</text>

      <text class="doctor-name" transform="translate(66 336) rotate(-11)"
        textLength="820" lengthAdjust="spacingAndGlyphs">Hugo Tolliver, MD</text>

      <text class="tagline" transform="translate(82 398) rotate(-8.6)"
        textLength="800" lengthAdjust="spacingAndGlyphs"><tspan class="t-blue">MODERN </tspan><tspan class="t-pink">MEDICINE, </tspan><tspan class="t-yellow">TRADITIONAL CARE</tspan></text>
    </svg>

    <address class="contact-panel">
      41587 Calder Ridge Road, Suite 215,<br>
      Mission Viejo, CA 92691<br>
      Phone: 949-555-0178<br>
      www.quillmarshvale.net
    </address>

    <div class="brand-panel">
      <span class="brand-mark" aria-hidden="true"></span>
      <span class="brand-name">
        <span class="brand-main">Quillmarsh Vale</span>
        <span class="brand-sub">MEDICAL GROUP</span>
      </span>
    </div>
  </main>
</body>
</html>
```